Website for The Copper Lantern

We need an impressive e-commerce website for our newly launched business "The Copper Lantern".
The Copper Lantern searches store-front and online retailers for diamond engagement rings according to the client's specified requirements. We want to save people time by doing the shopping around for them.
We can relate to, and we love, www.roomtrellis.com
Like roomtrellis.com, we want to offer website visitors a quick run-down on how the process works, then offer them to elect a service package and pay for that package on the spot.
Content pages:
HOME
HOW IT WORKS
DIAMOND GALLERY
ABOUT
FAQs
CONTACT
Inclusions: Our logo and Facebook and Instagram buttons
We want to be able to easily edit this website, We want it to display well on iPhone and android, We want it to be clean and striking.
Like our logo, we want our website to embody elegant masculinity.
Target Market(s)
Men in market for diamond ring purchase $5k - $50k
Industry/Entity Type
Business
Number of Pages Required
5+ page
Font styles to use
Look and feel

```html
<!DOCTYPE html>
<html lang="en">
<head>
<meta charset="utf-8">
<title>The Copper Lantern</title>
<link href="https://fonts.googleapis.com/css2?family=Cinzel:wght@400&family=PT+Serif:wght@400&display=swap" rel="stylesheet">
<style>
:root{
  --ink:#3a3a3a;
  --muted:#6d6d6d;
  --rule:#d9d9d9;
  --nav-bg:#efefef;
  --topline:#555;
  --btn:#8a8a8a;
  --white:#fff;
  --link:#2d5da8;
  --footer-bar:#8c8c8c;
}
*{margin:0;padding:0;box-sizing:border-box}
html,body{width:856px;height:1200px;overflow:hidden;background:var(--white)}
body{position:relative;font-family:"PT Serif",Georgia,serif;color:var(--ink)}
.display{font-family:"Cinzel",Georgia,serif;font-weight:400}
.abs{position:absolute}
.topline{left:0;top:0;width:856px;height:4px;background:var(--topline)}
.contact-line{left:10px;top:25px;font-size:11px;line-height:13px;color:var(--muted);font-family:"PT Serif",serif}
.btn-finance{left:650px;top:26px;width:200px;height:23px;background:var(--btn);color:var(--white);border-radius:4px;font-size:11px;letter-spacing:.5px;text-align:center;line-height:23px}
.nav{left:0;top:71px;width:856px;height:37px;background:var(--nav-bg)}
.nav a{position:absolute;top:12px;font-size:11.5px;color:var(--ink);text-decoration:none;letter-spacing:.4px}
.logo{left:373px;top:4px;width:80px;height:88px;background:var(--white);text-align:center}
.logo-mark{display:block;margin:14px auto 6px;width:22px;height:22px;border:1.5px solid var(--muted);border-radius:50%}
.logo-name{font-size:9.5px;line-height:11px;color:var(--ink);letter-spacing:.3px}
.hero{left:0;top:108px;width:856px;height:438px;background:radial-gradient(ellipse at 72% 50%,#e8e3e6 0%,#b9a9b1 22%,#c77b7e 45%,#c2686c 70%,#a85458 100%)}
.hero h1{position:absolute;left:24px;top:166px;font-size:27px;color:var(--white);letter-spacing:1px}
.hero .rule{position:absolute;left:26px;top:206px;width:290px;height:2px;background:var(--white)}
.hero p{position:absolute;left:25px;top:226px;width:310px;text-align:center;font-family:"Cinzel",serif;font-size:12.5px;line-height:22px;color:var(--white);letter-spacing:.4px}
.dots{position:absolute;left:410px;top:416px;display:flex;gap:5px}
.dots span{width:9px;height:9px;border-radius:50%;background:var(--white)}
.dots span.off{background:transparent;border:1.5px solid var(--white)}
.panel-selfie{left:6px;top:553px;width:344px;height:243px;background:linear-gradient(90deg,#262626 0%,#3a3a3a 55%,#8a8784 80%,#5b5957 100%)}
.panel-fire{left:361px;top:552px;width:489px;height:243px;background:linear-gradient(100deg,#6e6e6e 0%,#c9c9c9 30%,#e4e4e4 55%,#b8b8b8 80%,#8f8f8f 100%)}
.panel-title{position:absolute;font-size:19px;letter-spacing:.5px}
.panel-text{position:absolute;font-size:10px;line-height:13.5px}
.loose{left:0;top:805px;width:856px;height:257px;background:linear-gradient(90deg,#bdbdbd 0%,#e6e6e6 22%,#f6f6f6 45%,#f7f7f7 100%)}
.loose h2{position:absolute;right:59px;top:26px;font-size:31px;letter-spacing:1px;color:var(--ink)}
.loose p{position:absolute;left:221px;top:67px;width:585px;font-size:16px;line-height:20.7px;color:var(--ink)}
.footer{left:26px;top:1071px;width:799px;height:108px;border-top:1px solid var(--rule);border-bottom:1px solid var(--rule)}
.fcol{position:absolute;top:0;height:107px;border-right:1px solid var(--rule)}
.fcol:last-child{border-right:none}
.fhead{position:absolute;top:11px;font-size:7.5px;letter-spacing:1.2px;color:var(--muted);font-family:"Cinzel",serif}
.flist{position:absolute;font-size:7.3px;line-height:12px;color:var(--ink);list-style:none}
.store{position:absolute;left:10px;top:32px;font-size:8.8px;line-height:18.5px}
.store a{color:var(--link);font-style:italic;text-decoration:none}
.hours{position:absolute;left:11px;top:32px;font-size:7px;line-height:12.6px}
.social{position:absolute;left:12px;top:36px;display:flex;gap:3px}
.social span{width:12px;height:12px;border-radius:50%;background:#8f8f8f}
.copy{left:0;top:1182px;width:856px;height:18px;background:var(--footer-bar);color:var(--white);font-size:9.5px;text-align:center;line-height:18px}
</style>
</head>
<body>
<div class="abs topline"></div>
<div class="abs contact-line">T: (123) 555-0147<br>1180 LARKMOOR RD, BROOKHAVEN, IN 47802</div>
<div class="abs btn-finance display">APPLY FOR FINANCING</div>

<nav class="abs nav display">
  <a style="left:53px">HOME</a>
  <a style="left:150px">ABOUT</a>
  <a style="left:243px">HOW IT WORKS</a>
  <a style="left:498px">FAQS</a>
  <a style="left:589px">DIAMOND GALLERY</a>
  <a style="left:746px">CONTACT</a>
</nav>
<div class="abs logo">
  <span class="logo-mark"></span>
  <div class="logo-name display">THE COPPER<br>LANTERN</div>
</div>

<section class="abs hero" role="img" aria-label="Photograph of two diamond engagement rings with pink blossoms on a rose background">
  <h1 class="display">ENGAGEMENT RINGS</h1>
  <div class="rule"></div>
  <p>THE FIRST BIG STEP IN A LIFETIME OF LOVE<br>DISCOVER OUT FAVOURITE COLLECTIONS</p>
  <div class="dots"><span></span><span class="off"></span><span></span></div>
</section>

<section class="abs panel-selfie" role="img" aria-label="Photograph of a woman's hand showing an engagement ring">
  <h3 class="panel-title display" style="left:17px;top:79px;color:var(--white)">THE PERFECT RING SELFIE</h3>
  <p class="panel-text" style="left:20px;top:107px;width:240px;color:var(--white)">Learn how to take the perfect engagement ring selfie with tips from Brookhaven Wedding photographer Maren Holt.</p>
</section>

<section class="abs panel-fire" role="img" aria-label="Black and white photograph of a hand wearing a diamond ring">
  <h3 class="panel-title display" style="left:190px;top:78px;font-size:28px;color:#2f2f2f">EMBER &amp; FACET</h3>
  <p class="panel-text" style="left:195px;top:119px;width:265px;color:#2f2f2f">The Lantern Gallery is proud to be Brookhaven's exclusive source for Ember &amp; Facet, The World's Most Perfectly Cut Diamond.</p>
</section>

<section class="abs loose" role="img" aria-label="Soft grey photograph of scattered loose diamonds">
  <h2 class="display">LOOSE DIAMONDS</h2>
  <p>A diamond is special, whether it's given in an engagement ring as a promise of forever or chosen as the centerpiece of a custom design to be treasured for years to come. We understand that selecting this stone, no matter the occasion, is momentous. Our selection, price and quality ensure that you choose from only the best and our in-house diamond experts help you find the perfect diamond for your special moment.</p>
</section>

<footer class="abs footer">
  <div class="fcol" style="left:0;width:199px">
    <ul class="flist" style="left:11px;top:12px"><li>Engagement</li><li>Diamonds</li><li>Jewelry</li><li>Events</li></ul>
    <ul class="flist" style="left:99px;top:12px"><li>Wedding</li><li>Our Designers</li><li>About</li><li>Contact</li></ul>
  </div>
  <div class="fcol" style="left:199px;width:200px">
    <div class="fhead" style="left:12px">CUSTOMER SERVICE</div>
    <ul class="flist" style="left:12px;top:30px"><li>Warranty</li><li>Charities</li><li>Privacy Policy</li><li>5 + 5 = Love Card</li></ul>
    <ul class="flist" style="left:100px;top:30px"><li>Financing</li><li>Jewelry Care</li><li>Look Books</li></ul>
  </div>
  <div class="fcol" style="left:399px;width:133px">
    <div class="fhead" style="left:10px">OUR STORE:</div>
    <div class="store">1180 Larkmoor Rd.<br>Brookhaven, IN 47802<br><a>Get Directions</a></div>
  </div>
  <div class="fcol" style="left:532px;width:133px">
    <div class="fhead" style="left:11px">OUR HOURS:</div>
    <div class="hours">Monday – Thursday: 10AM–6PM<br>Friday: 10AM–7PM<br>Saturday: 10AM–5PM<br>Sunday: Closed</div>
  </div>
  <div class="fcol" style="left:665px;width:134px">
    <div class="fhead" style="left:12px">STAY IN TOUCH:</div>
    <div class="social"><span></span><span></span><span></span><span></span><span></span><span></span><span></span></div>
  </div>
</footer>
<div class="abs copy">©2016 The Copper Lantern. All Rights Reserved.</div>
</body>
</html>
```